CrestwayGuides Summer Brunch

This flyer is designed to market the upcoming conference in July

Target Market(s)

African American Christian Men and Women

Font styles to use
Decorative

Requirements
Must have
• This flyer is to represent both men and women as follows:
• Although offered on the same day and same location - Men and Women must appear two meetings in one location
• 1. SOB - Sons of Bright
• 2. GAVU - Gentle and Very Uplifted - Women
• Theme: "2020 - Rising With Grace" (Ephesians 6:10-15)
• Date: June 27, 2020
Nice to have
• *Distinct between the two meetings in one
• * Unified brand coupled with Men and Women targets
• * Vibrant, energized, active flyer to communicate promise and hope
Should not have
• Profanity, clip art, etc.

```html
<!DOCTYPE html>
<html lang="en">
<head>
<meta charset="utf-8">
<title>CrestwayGuides – Rising With Grace</title>
<link href="https://fonts.googleapis.com/css2?family=Playfair+Display:ital,wght@0,400;0,700;0,900;1,400;1,700&family=Montserrat:wght@400;500;600&family=Cormorant+Garamond:wght@500&display=swap" rel="stylesheet">
<style>
  :root{
    --ink:#1b1219;
    --plum:#2b1d29;
    --gold:#c98a2e;
    --gold-deep:#a8661b;
    --bronze:#7a4418;
    --white:#ffffff;
    --cream:#f3ece2;
    --rule:#9a8c90;
  }
  *{margin:0;padding:0;box-sizing:border-box}
  html,body{width:934px;height:1200px;overflow:hidden;background:var(--ink)}
  .flyer{position:relative;width:934px;height:1200px;overflow:hidden;
    background:radial-gradient(ellipse at 50% 60%,var(--plum) 0%,var(--ink) 70%);
    font-family:"Playfair Display",serif;color:var(--white)}
  .shapes{position:absolute;inset:0}

  .brand{position:absolute;left:52px;top:72px;width:282px;height:146px;
    display:flex;flex-direction:column;align-items:center;justify-content:center;gap:12px}
  .brand-name{display:flex;align-items:center;gap:10px;
    font-family:"Montserrat",sans-serif;font-weight:500;font-size:27px;color:var(--white);line-height:1}
  .brand-mark{width:12px;height:12px;border-radius:50%;background:var(--gold)}
  .brand-tagline{font-family:"Montserrat",sans-serif;font-size:8.5px;letter-spacing:0.8px;color:var(--gold)}

  .date-rule{position:absolute;left:700px;top:52px;width:104px;height:4px;background:var(--gold)}
  .date-month{position:absolute;left:654px;top:104px;width:110px;transform:rotate(-90deg);
    font-size:32px;letter-spacing:3px;text-align:center;color:var(--white);line-height:1}
  .date-day{position:absolute;left:738px;top:52px;font-size:120px;font-weight:700;line-height:1;color:var(--white)}
  .date-year{position:absolute;left:734px;top:172px;width:122px;height:42px;background:var(--gold);
    color:var(--ink);font-size:31px;font-weight:700;text-align:center;line-height:42px}

  .notice{position:absolute;left:0;width:934px;text-align:center}
  .notice-lead{top:296px;font-family:"Cormorant Garamond",serif;font-size:24px}
  .notice-rule{top:326px;font-style:italic;font-weight:700;color:var(--gold);font-size:19px}
  .divider{position:absolute;left:178px;width:572px;border-top:2px dotted var(--rule)}
  .meetings{position:absolute;left:0;top:396px;width:934px;text-align:center;
    font-family:"Montserrat",sans-serif;font-size:28px;line-height:39px}
  .meetings b{font-weight:600;color:var(--gold)}

  .theme-year{position:absolute;left:264px;top:564px;width:156px;height:42px;border-radius:21px;
    background:var(--white);color:var(--ink);font-size:30px;font-weight:700;text-align:center;line-height:42px;letter-spacing:3px}
  .theme-title{position:absolute;left:142px;top:586px;font-weight:700;font-size:116px;line-height:118px;color:var(--gold);letter-spacing:-1px}
  .theme-title span{display:block}
  .theme-title .line2{padding-left:66px}
  .quote{position:absolute;font-size:96px;font-weight:700;color:var(--gold);line-height:1}
  .quote-open{left:128px;top:522px}
  .quote-close{left:764px;top:768px}
  .verse{position:absolute;left:0;top:850px;width:934px;text-align:center;
    font-family:"Montserrat",sans-serif;font-size:17px;letter-spacing:8px}

  .contact{position:absolute;left:94px;font-size:25px;font-style:italic;font-weight:700;color:var(--ink);
    display:flex;align-items:center;gap:10px}
  .contact i{width:20px;height:20px;border-radius:50%;border:2px solid var(--ink);display:inline-block}
  .contact i.solid{background:var(--ink)}
  .web{top:1062px}.social{top:1108px}
  .phone{position:absolute;left:604px;top:1074px;font-size:38px;font-weight:700;color:var(--ink);line-height:1}
</style>
</head>
<body>
<main class="flyer">
  <svg class="shapes" width="934" height="1200" viewBox="0 0 934 1200">
    <defs>
      <linearGradient id="hands" x1="0" y1="0" x2="0" y2="1">
        <stop offset="0" stop-color="#3b2e30"/><stop offset="1" stop-color="#1b1219" stop-opacity="0"/>
      </linearGradient>
      <linearGradient id="church" x1="0" y1="0" x2="1" y2="1">
        <stop offset="0" stop-color="#e6d2b0"/><stop offset="0.5" stop-color="#b98a48"/><stop offset="1" stop-color="#6e4a2c"/>
      </linearGradient>
      <linearGradient id="reader" x1="0" y1="0" x2="1" y2="1">
        <stop offset="0" stop-color="#d88a3a"/><stop offset="0.6" stop-color="#8a4a25"/><stop offset="1" stop-color="#4a2a1e"/>
      </linearGradient>
      <linearGradient id="goldWedge" x1="0" y1="0" x2="1" y2="1">
        <stop offset="0" stop-color="#d69a3e"/><stop offset="0.7" stop-color="#c58632"/><stop offset="1" stop-color="#3a2416"/>
      </linearGradient>
      <linearGradient id="crowd" x1="0" y1="0" x2="0" y2="1">
        <stop offset="0" stop-color="#2b1d29" stop-opacity="0"/><stop offset="1" stop-color="#3a2a33" stop-opacity="0.8"/>
      </linearGradient>
    </defs>

    <rect x="52" y="72" width="282" height="146" fill="#000"/>
    <rect role="img" aria-label="Photo of praying hands holding rosary beads" x="378" y="0" width="180" height="290" fill="url(#hands)"/>
    <line x1="872" y1="62" x2="934" y2="14" stroke="#fff" stroke-width="3"/>

    <!-- right bronze tiles -->
    <rect x="820" y="300" width="200" height="200" rx="30" fill="var(--bronze)" transform="rotate(45 920 400)"/>
    <rect x="840" y="680" width="180" height="180" rx="28" fill="var(--bronze)" transform="rotate(45 930 770)"/>
    <rect x="752" y="450" width="256" height="256" rx="38" fill="#fff" transform="rotate(45 880 578)"/>
    <rect role="img" aria-label="Photo of a congregation in an ornate church" x="766" y="464" width="228" height="228" rx="30" fill="url(#church)" transform="rotate(45 880 578)"/>

    <!-- left bronze tile -->
    <rect x="-60" y="600" width="180" height="180" rx="28" fill="#5a3212" transform="rotate(45 30 690)"/>
    <line x1="0" y1="612" x2="30" y2="584" stroke="#fff" stroke-width="3"/>

    <!-- bottom gold wedge -->
    <path d="M0 930 Q40 880 140 900 L420 965 Q520 990 560 1200 L0 1200 Z" fill="url(#goldWedge)"/>
    <rect x="-62" y="718" width="240" height="240" rx="36" fill="#fff" transform="rotate(45 58 838)"/>
    <rect role="img" aria-label="Photo of a smiling woman reading a Bible" x="-49" y="731" width="214" height="214" rx="30" fill="url(#reader)" transform="rotate(45 58 838)"/>

    <rect role="img" aria-label="Silhouettes of a worshipping crowd with raised hands" x="400" y="900" width="534" height="156" fill="url(#crowd)"/>

    <!-- phone band -->
    <path d="M522 1056 L934 1056 L934 1142 L522 1142 Q548 1100 522 1056 Z" fill="#fff"/>
    <rect x="550" y="1080" width="36" height="36" rx="6" fill="var(--ink)"/>
    <path d="M561 1088 q-3 3 0 9 q4 7 10 10 q5 2 7 -1 l-3 -4 l-4 2 q-4 -2 -6 -6 l2 -4 z" fill="#fff"/>
  </svg>

  <header class="brand">
    <span class="brand-name"><span class="brand-mark"></span>CrestwayGuides</span>
    <span class="brand-tagline">GUIDING HEARTS, BUILDING STRONGER FAMILIES</span>
  </header>

  <div class="date-rule"></div>
  <div class="date-month">JUNE</div>
  <div class="date-day">27</div>
  <div class="date-year">2020</div>

  <p class="notice notice-lead">Although offered on the same day and same location -</p>
  <p class="notice notice-rule">Men and Women must appear two meetings in one location</p>

  <div class="divider" style="top:382px"></div>
  <p class="meetings"><b>SOB -</b> Sons of Bright<br><b>GAVU -</b> Gentle and Very Uplifted - Women</p>
  <div class="divider" style="top:488px"></div>

  <span class="quote quote-open">“</span>
  <div class="theme-year">2020</div>
  <h1 class="theme-title"><span class="line1">Rising</span><span class="line2">With Grace</span></h1>
  <span class="quote quote-close">”</span>
  <p class="verse">( Ephesians 6:10-15 )</p>

  <p class="contact web"><i></i>CrestwayGuides.com</p>
  <p class="contact social"><i class="solid"></i>CrestwayGuides.com</p>
  <p class="phone">555.014.2736</p>
</main>
</body>
</html>
```